Business Card Design Project

Need professional business card and Employee Badge design for a young dynamic and emp friendly IT Services company.

Target Market(s)

IT, Corporate

Industry/Entity Type

Business

Requirements
Must have
• Modern, Sleek, Prfessional, IT services
Should not have
• Too much diffrent colors

```html
<!DOCTYPE html>
<html lang="en">
<head>
<meta charset="utf-8">
<title>Korvel Technologies – Business Card</title>
<link rel="stylesheet" href="https://fonts.googleapis.com/css2?family=Didact+Gothic&family=Mulish:wght@700;800&display=swap">
<style>
  :root {
    --backdrop: #e9e6e4;
    --card: #ffffff;
    --brand-red: #c8202f;
    --ink: #1f1f1f;
    --muted-line: #ececec;
    --band-dark: #4a4a4a;
    --accent-tan: #e6d2c3;
    --accent-grey: #e4e3e5;
    --edge-brown: #b5532b;
  }
  * { box-sizing: border-box; margin: 0; padding: 0; }
  html, body { width: 1200px; height: 800px; overflow: hidden; }
  body {
    background: var(--backdrop);
    font-family: "Didact Gothic", "Century Gothic", sans-serif;
    position: relative;
  }
  .business-card {
    position: absolute;
    left: 150px; top: 143px;
    width: 900px; height: 514px;
    background: var(--card);
    box-shadow: 0 10px 30px rgba(0,0,0,.18);
    overflow: hidden;
  }
  .card-graphics { position: absolute; inset: 0; }
  .brand-block {
    position: absolute;
    left: 60px; top: 70px;
    width: 350px; height: 145px;
    border: 1px solid var(--muted-line);
    display: flex; align-items: center; gap: 14px;
    padding-left: 26px;
  }
  .brand-mark {
    width: 16px; height: 16px;
    background: var(--brand-red);
    flex: none;
  }
  .brand-name {
    font-family: "Mulish", sans-serif;
    font-weight: 800;
    color: var(--brand-red);
    line-height: 1.05;
    font-size: 40px;
    letter-spacing: .5px;
  }
  .brand-name .brand-sub { display: block; font-size: 22px; letter-spacing: 5px; }
  .contact-block { position: absolute; left: 62px; top: 238px; }
  .person-name {
    font-family: "Mulish", sans-serif;
    font-weight: 700;
    color: var(--brand-red);
    font-size: 27px;
  }
  .person-role { font-size: 18px; color: var(--ink); margin: 2px 0 8px 14px; }
  .contact-list { list-style: none; }
  .contact-list li {
    display: flex; align-items: center; gap: 12px;
    font-size: 21px; color: var(--ink);
    height: 29px;
  }
  .contact-list svg { width: 20px; height: 20px; flex: none; }
</style>
</head>
<body>
  <article class="business-card">
    <svg class="card-graphics" viewBox="0 0 900 514" aria-hidden="true">
      <polygon points="590,40 640,40 612,330" fill="var(--accent-tan)"/>
      <polygon points="660,95 840,305 660,340" fill="var(--accent-grey)"/>
      <polygon points="0,452 900,372 900,514 0,514" fill="var(--band-dark)"/>
      <polygon points="0,446 900,366 900,374 0,454" fill="var(--brand-red)"/>
      <rect x="0" y="506" width="900" height="8" fill="var(--edge-brown)"/>
    </svg>

    <div class="brand-block">
      <span class="brand-mark"></span>
      <p class="brand-name">korvel<span class="brand-sub">technologies</span></p>
    </div>

    <section class="contact-block">
      <h1 class="person-name">Dana Whitfield</h1>
      <p class="person-role">Manager</p>
      <ul class="contact-list">
        <li>
          <svg viewBox="0 0 24 24"><path fill="var(--brand-red)" d="M6.6 10.8a15 15 0 0 0 6.6 6.6l2.2-2.2c.3-.3.7-.4 1-.2 1.1.4 2.3.6 3.6.6.6 0 1 .4 1 1V20c0 .6-.4 1-1 1A17 17 0 0 1 3 4c0-.6.4-1 1-1h3.5c.6 0 1 .4 1 1 0 1.3.2 2.5.6 3.6.1.3 0 .7-.2 1z"/></svg>
          1520 447 316
        </li>
        <li>
          <svg viewBox="0 0 24 24"><path fill="var(--brand-red)" d="M12 3 2 12h3v9h5v-6h4v6h5v-9h3z"/></svg>
          PO Box 40518 AL 35214
        </li>
        <li>
          <svg viewBox="0 0 24 24"><rect x="2" y="5" width="20" height="14" rx="2" fill="var(--brand-red)"/><path d="M3 6l9 7 9-7" stroke="#fff" stroke-width="1.6" fill="none"/></svg>
          hello@korveltech.com
        </li>
        <li>
          <svg viewBox="0 0 24 24"><g fill="none" stroke="var(--brand-red)" stroke-width="1.8"><circle cx="12" cy="12" r="9.5"/><ellipse cx="12" cy="12" rx="4" ry="9.5"/><path d="M2.5 12h19M4 7h16M4 17h16"/></g></svg>
          www.korveltech.com
        </li>
      </ul>
    </section>
  </article>
</body>
</html>
```